Flyer Design Project

We are custom home contractors and renovators, and been doing it for many years, in toronto and the greater toronto area. I need a flyer design that incorperates our years of experience,customer satisfaction,being reliable ,competitive in pricing. We can,and do work with the customers from the ground up ,meaning we have architects,designers, and engineers we work with. We have many references of satisfied customers.
We have businesscards and a website that was just started and really not finished,but is up needs work.

```html
<!DOCTYPE html>
<html lang="en">
<head>
<meta charset="utf-8">
<title>Home Contractors and Renovators Flyer</title>
<link href="https://fonts.googleapis.com/css2?family=Tinos:ital,wght@0,400;0,700;1,400&family=Archivo+Black&display=swap" rel="stylesheet">
<style>
  :root {
    --blue: #1aa3e8;
    --blue-deep: #0a6fc2;
    --navy: #0d4f8f;
    --sky-top: #0f5fae;
    --sky-low: #5fb8ea;
    --orange: #f7a21b;
    --orange-soft: #fbb944;
    --sand: #efe3c4;
    --ink-blue: #1f5fa8;
    --white: #ffffff;
    --paper: #f4f4f4;
  }
  * { margin: 0; padding: 0; box-sizing: border-box; }
  html, body { width: 851px; height: 1200px; overflow: hidden; background: var(--white); }
  .flyer {
    position: relative; width: 851px; height: 1200px; overflow: hidden;
    background: var(--white); font-family: "Tinos", "Times New Roman", serif;
  }
  .abs { position: absolute; }

  .brand {
    left: 48px; top: 72px; color: var(--blue); font-size: 36px; line-height: 1.3;
    letter-spacing: 0.5px; text-transform: uppercase;
  }
  .top-contact { right: 26px; top: 8px; text-align: right; color: var(--orange); }
  .top-contact .phone { font-size: 27px; font-weight: 700; }
  .top-contact .email { font-size: 15px; font-weight: 700; margin-top: 2px; }

  .skyline-scene {
    left: 0; top: 190px; width: 851px; height: 420px;
    background: linear-gradient(180deg, var(--sky-top) 0%, #2f8fd6 55%, var(--sky-low) 72%, #1560a8 100%);
  }
  .waves { left: 0; top: 0; width: 851px; height: 700px; }

  .why-best-col {
    left: 0; top: 640px; width: 270px; height: 480px; background: var(--blue);
  }
  .why-best-label {
    left: 0; top: 720px; width: 270px; height: 58px; background: var(--sand);
    color: var(--blue); font-size: 34px; text-align: center; line-height: 58px;
  }
  .team-list { left: 18px; top: 805px; list-style: none; }
  .team-list li {
    display: flex; align-items: center; gap: 12px;
    color: #fff6d8; font-size: 35px; line-height: 46px;
  }
  .team-note {
    left: 18px; top: 975px; width: 240px; color: var(--navy);
    font-style: italic; font-size: 19px; line-height: 1.4;
  }

  .why-us-title {
    left: 415px; top: 588px; color: var(--orange); font-size: 38px; letter-spacing: 1px;
  }
  .benefit-list { left: 310px; top: 655px; list-style: none; }
  .benefit-list li {
    display: flex; align-items: center; gap: 18px;
    color: var(--ink-blue); font-size: 26px; height: 66px;
  }
  .work-note {
    left: 305px; top: 988px; width: 520px; color: var(--blue-deep);
    font-style: italic; font-weight: 700; font-size: 21px; line-height: 1.4;
  }

  .footer-brand {
    left: 0; top: 1120px; width: 270px; height: 80px; background: var(--sand);
    color: var(--orange); font-size: 20px; line-height: 1.35;
    padding: 8px 0 0 28px; text-transform: uppercase;
  }
  .footer-cta {
    left: 270px; top: 1120px; width: 270px; height: 80px; background: var(--orange);
    font-family: "Archivo Black", "Arial Black", sans-serif; padding: 4px 0 0 22px;
  }
  .footer-cta .small { color: var(--navy); font-size: 22px; line-height: 1; }
  .footer-cta .big { color: var(--orange-soft); font-size: 48px; line-height: 1; color: #fde3a8; font-style: italic; }
  .footer-call {
    left: 540px; top: 1120px; width: 311px; height: 80px; background: var(--paper);
    color: var(--navy); font-size: 27px; font-weight: 700; text-align: center; line-height: 80px;
  }
</style>
</head>
<body>
<div class="flyer">
  <div class="abs skyline-scene" role="img" aria-label="Night city skyline of Toronto with a full moon over the water"></div>

  <svg class="abs waves" viewBox="0 0 851 700" aria-hidden="true">
    <!-- upper band -->
    <path d="M0 0 H851 V100 C640 110 420 140 0 190 Z" fill="#ffffff"/>
    <path d="M0 190 C420 140 640 110 851 100 V128 C640 135 420 165 0 222 Z" fill="#f7a21b"/>
    <path d="M0 222 C420 165 640 135 851 128 V156 C640 165 420 200 0 250 Z" fill="#1aa3e8"/>
    <!-- lower band -->
    <path d="M0 560 C260 520 520 505 851 520 V700 H0 Z" fill="#ffffff"/>
    <path d="M0 545 C260 510 520 490 851 500 V545 C560 530 300 555 0 610 Z" fill="#1aa3e8"/>
    <path d="M0 610 C300 555 560 530 851 545 V568 C560 560 320 585 0 650 Z" fill="#f7a21b"/>
    <path d="M0 650 C320 585 560 560 851 568 V700 H0 Z" fill="#ffffff"/>
  </svg>

  <div class="abs brand">Home Contractors<br>and Renovators</div>
  <div class="abs top-contact">
    <div class="phone">Call Us : 555-010-2030</div>
    <div class="email">Email : hello@homebuildpro.ca</div>
  </div>

  <div class="abs why-best-col"></div>
  <div class="abs why-best-label">WHY BEST</div>
  <ul class="abs team-list">
    <li><svg width="30" height="24" viewBox="0 0 30 24"><path d="M3 12 L11 20 L27 4" stroke="#f7a21b" stroke-width="6" fill="none" stroke-linecap="round" stroke-linejoin="round"/></svg>Architects</li>
    <li><svg width="30" height="24" viewBox="0 0 30 24"><path d="M3 12 L11 20 L27 4" stroke="#f7a21b" stroke-width="6" fill="none" stroke-linecap="round" stroke-linejoin="round"/></svg>Designers</li>
    <li><svg width="30" height="24" viewBox="0 0 30 24"><path d="M3 12 L11 20 L27 4" stroke="#f7a21b" stroke-width="6" fill="none" stroke-linecap="round" stroke-linejoin="round"/></svg>Engineers</li>
  </ul>
  <p class="abs team-note">Doing it for many years, in toronto and the greater toronto area ..</p>

  <div class="abs why-us-title">WHY US</div>
  <ul class="abs benefit-list">
    <li><svg width="34" height="26" viewBox="0 0 34 26"><path d="M3 13 L12 22 L31 4" stroke="#f7a21b" stroke-width="6" fill="none" stroke-linecap="round" stroke-linejoin="round"/></svg>Our years of experience</li>
    <li><svg width="34" height="26" viewBox="0 0 34 26"><path d="M3 13 L12 22 L31 4" stroke="#f7a21b" stroke-width="6" fill="none" stroke-linecap="round" stroke-linejoin="round"/></svg>Customer satisfaction</li>
    <li><svg width="34" height="26" viewBox="0 0 34 26"><path d="M3 13 L12 22 L31 4" stroke="#f7a21b" stroke-width="6" fill="none" stroke-linecap="round" stroke-linejoin="round"/></svg>Being reliable</li>
    <li><svg width="34" height="26" viewBox="0 0 34 26"><path d="M3 13 L12 22 L31 4" stroke="#f7a21b" stroke-width="6" fill="none" stroke-linecap="round" stroke-linejoin="round"/></svg>Competitive in pricing</li>
  </ul>
  <p class="abs work-note">We can,and do work with the customers from the ground up &amp; We have many references of satisfied customers.</p>

  <div class="abs footer-brand">Home Contractors<br>and Renovators</div>
  <div class="abs footer-cta">
    <div class="small">Contact Us</div>
    <div class="big">Today !</div>
  </div>
  <div class="abs footer-call">Call Us : 555-010-2030</div>
</div>
</body>
</html>
```